Moving Company Website

We need a webdesign for an established moving company in the Bay Area. We have chosen a wordpress template (see attached) and would like to revamp the design to give it a touch and feel of a leading moving company.
The design should be inspired by the following companies:
http://www.brightvanline.com/
http://www.kpcarriers.com/
Updates

The design should be based on the following WordPress template:

http://www.layoutforge.com/demo/35782.html

And based on the image I have attached.

We will get the template PSD after we will choose a designer.

Thanks
Marcus 

Industry/Entity Type

Moving Company

Requirements
Must have
• Request a quote form must be implemented in all pages
inner pages with destinations

```html
<!DOCTYPE html>
<html lang="en">
<head>
<meta charset="utf-8">
<title>Swiftline Movers</title>
<link rel="stylesheet" href="https://fonts.googleapis.com/css2?family=Questrial&family=Arimo:wght@400;700&display=swap">
<style>
:root{
  --green:#0d8a3a;
  --ink:#1c1c1c;
  --text:#2b2b2b;
  --muted:#b5b5b5;
  --rule:#b9b9b9;
  --panel:#f4f4f4;
  --band:#f3f3f3;
  --white:#ffffff;
}
*{box-sizing:border-box;margin:0;padding:0}
html,body{width:747px;height:1200px;overflow:hidden;background:var(--white)}
body{position:relative;font-family:"Arimo",Arial,sans-serif;color:var(--text);font-size:10px;line-height:1.45}
.abs{position:absolute}
.display{font-family:"Questrial",sans-serif;color:var(--ink)}
.rule{position:absolute;height:0;border-top:1px dashed var(--rule)}

/* header */
.brand{left:29px;top:18px;width:80px;text-align:left}
.brand-mark{display:block;width:30px;height:30px;border-radius:50%;background:var(--ink);margin:0 0 4px 12px}
.brand-name{font-family:"Questrial",sans-serif;font-size:11px;line-height:1.05;color:var(--green);font-weight:400;letter-spacing:.2px}
.social-label{left:500px;top:18px;font-family:"Questrial",sans-serif;font-size:13px;color:var(--muted)}
.social{left:623px;top:15px;display:flex;gap:5px}
.social span{width:20px;height:20px;border-radius:3px;background:#c4c4c4;display:block}
.nav{left:165px;top:58px;display:flex;align-items:center;font-family:"Questrial",sans-serif;font-size:14px;color:var(--ink)}
.nav a{color:inherit;text-decoration:none;position:absolute;white-space:nowrap}
.nav .current{font-weight:700;font-family:"Arimo",sans-serif;font-size:13.5px}
.nav .marker{position:absolute;left:0;top:4px;width:9px;height:11px;background:var(--green)}

/* hero */
.hero{left:29px;top:109px;width:453px;height:258px;border-radius:3px;background:linear-gradient(110deg,#6f9aa6 0%,#c9b79a 35%,#e8d3b6 55%,#8e99a0 80%,#5c6a72 100%)}
.quote{left:497px;top:109px;width:221px;height:258px;background:var(--panel)}
.quote h2{position:absolute;left:27px;top:16px;font-family:"Questrial",sans-serif;font-weight:400;font-size:13px;color:var(--ink);letter-spacing:.2px}
.quote .rule{left:27px;width:160px}
.field{position:absolute;left:27px;width:160px;height:19px;background:var(--white);font-size:9.5px;padding:3px 6px;color:var(--text)}
.field.select{display:flex;justify-content:space-between;align-items:center}
.submit{position:absolute;left:27px;top:226px;width:62px;height:18px;background:var(--green);color:var(--white);font-size:9.5px;text-align:center;line-height:18px}

/* service columns */
.col{position:absolute;top:398px;width:161px}
.col h3{font-family:"Questrial",sans-serif;font-weight:400;font-size:19px;color:var(--ink);height:36px}
.photo{width:161px;height:114px;border-radius:3px}
.col p{margin-top:14px;font-size:9.6px;line-height:1.52;height:71px;overflow:hidden}
.more{position:absolute;font-size:8.5px;font-weight:700;color:var(--ink);display:flex;align-items:center;gap:16px}
.go{width:14px;height:11px;border-radius:6px;background:var(--green);display:inline-flex;align-items:center;justify-content:center}
.list{list-style:none;margin-top:14px;font-size:9.6px;line-height:1.52}
.list li{display:flex;align-items:center;gap:7px}
.chev{width:6px;height:8px;flex:none}

/* why us */
.why-title{left:29px;top:700px;font-size:19px}
.why-lead{left:29px;top:738px;font-family:"Questrial",sans-serif;font-size:14.5px;line-height:1.2;color:var(--muted)}
.why-copy{top:793px;width:284px;font-size:9.8px;line-height:1.5}
.faq{left:634px;top:743px;width:82px;height:84px;border-radius:12px;background:#f1f1f1;color:#fff;font-family:"Arimo",sans-serif;font-weight:700;font-size:68px;line-height:84px;text-align:center}

/* info band */
.band{left:0;top:911px;width:747px;height:227px;background:var(--band)}
.divider{position:absolute;top:911px;width:2px;height:227px;background:var(--white)}
.info{position:absolute;top:934px;width:160px}
.info h3{font-family:"Questrial",sans-serif;font-weight:400;font-size:19px;color:var(--ink);margin-bottom:12px}
.info p{font-size:9.6px;line-height:1.5;margin-bottom:12px}
.bubble{width:148px;height:64px;background:var(--white);border-radius:3px;position:relative;padding:17px 10px 0;font-size:9.6px;line-height:1.5}
.bubble::after{content:"";position:absolute;left:10px;bottom:-8px;border-left:8px solid var(--white);border-bottom:8px solid transparent}
.author{margin-top:12px;color:var(--muted);font-size:9.6px}
.ticks{list-style:none;font-size:9.6px;line-height:1.5}
.ticks li{display:flex;gap:6px;margin-bottom:11px}
.dot{width:11px;height:11px;border-radius:50%;background:var(--green);flex:none;margin-top:2px;display:flex;align-items:center;justify-content:center}

/* footer */
.foot-brand{left:33px;top:1150px}
.foot-brand .brand-mark{width:24px;height:24px;margin:0 0 3px 10px}
.foot-brand .brand-name{font-size:9.5px}
.copy{left:93px;top:1166px;font-size:9.8px}
.foot-nav{top:1166px;font-size:10px;color:var(--ink)}
</style>
</head>
<body>

<header>
  <div class="abs brand">
    <span class="brand-mark"></span>
    <div class="brand-name">SWIFTLINE<br>MOVERS</div>
  </div>
  <div class="abs social-label">socialize with us</div>
  <div class="abs social" aria-label="Social networks"><span></span><span></span><span></span><span></span></div>
  <div class="rule" style="left:107px;top:48px;width:609px"></div>
  <nav class="abs nav">
    <span class="marker"></span>
    <a class="current" style="left:19px">Home</a>
    <a style="left:88px">About us</a>
    <a style="left:175px">Services</a>
    <a style="left:259px">Products</a>
    <a style="left:346px">Partners</a>
    <a style="left:427px">News</a>
    <a style="left:493px">Contacts</a>
  </nav>
  <div class="rule" style="left:29px;top:89px;width:687px"></div>
</header>

<main>
  <div class="abs hero" role="img" aria-label="Portrait of a smiling customer in a bright office"></div>

  <form class="abs quote">
    <h2>REQUEST AN INTIMATE</h2>
    <div class="rule" style="top:44px"></div>
    <div class="field" style="top:67px">First name</div>
    <div class="field" style="top:96px">Last name</div>
    <div class="field" style="top:126px">Phone</div>
    <div class="field" style="top:155px">Email</div>
    <div class="field select" style="top:184px">Select service
      <svg width="8" height="6" viewBox="0 0 8 6"><path d="M1 1l3 3 3-3" fill="none" stroke="#222" stroke-width="1.6"/></svg>
    </div>
    <div class="rule" style="top:209px"></div>
    <div class="submit">Submit</div>
  </form>

  <section class="col" style="left:29px">
    <h3>Moving</h3>
    <div class="photo" role="img" aria-label="Moving team representative in office" style="background:linear-gradient(120deg,#e9edf0,#c9ced3 50%,#f1f2f3)"></div>
    <p>It is a long established fact that a reader will be distracted by the readable content of a page when looking at its layout. The point of using Lorem Ipsum is that</p>
  </section>
  <section class="col" style="left:204px">
    <h3>Storage</h3>
    <div class="photo" role="img" aria-label="Storage staff group" style="background:linear-gradient(120deg,#dfe3e7,#b9a89a 50%,#d5dadf)"></div>
    <p>It is a long established fact that a reader will be distracted by the readable content of a page when looking at its layout. The point of using Lorem Ipsum is that</p>
  </section>
  <section class="col" style="left:380px">
    <h3>Services</h3>
    <div class="photo" role="img" aria-label="Happy couple customers" style="background:linear-gradient(120deg,#dfe6ec,#c7a68c 50%,#a9b0b6)"></div>
    <p>It is a long established fact that a reader will be distracted by the readable content of a page when looking at its layout. The point of using Lorem Ipsum is that</p>
  </section>
  <section class="col" style="left:556px">
    <h3>Video</h3>
    <div class="photo" role="img" aria-label="Company team video preview" style="background:linear-gradient(120deg,#8d959c,#3d4349 50%,#a7adb2)"></div>
    <ul class="list">
      <li><svg class="chev" viewBox="0 0 6 8"><path d="M1 1l3 3-3 3" fill="none" stroke="#1c1c1c" stroke-width="1.8"/></svg>Our presentation video</li>
      <li><svg class="chev" viewBox="0 0 6 8"><path d="M1 1l3 3-3 3" fill="none" stroke="#1c1c1c" stroke-width="1.8"/></svg>Moving video</li>
      <li><svg class="chev" viewBox="0 0 6 8"><path d="M1 1l3 3-3 3" fill="none" stroke="#1c1c1c" stroke-width="1.8"/></svg>Its easy video</li>
    </ul>
  </section>

  <div class="more" style="left:28px;top:649px">More info <span class="go"><svg width="6" height="7" viewBox="0 0 6 7"><path d="M1 1l3 2.5-3 2.5" fill="none" stroke="#fff" stroke-width="1.5"/></svg></span></div>
  <div class="more" style="left:204px;top:649px">More info <span class="go"><svg width="6" height="7" viewBox="0 0 6 7"><path d="M1 1l3 2.5-3 2.5" fill="none" stroke="#fff" stroke-width="1.5"/></svg></span></div>
  <div class="more" style="left:380px;top:649px">More info <span class="go"><svg width="6" height="7" viewBox="0 0 6 7"><path d="M1 1l3 2.5-3 2.5" fill="none" stroke="#fff" stroke-width="1.5"/></svg></span></div>
  <div class="more" style="left:556px;top:619px">More info <span class="go"><svg width="6" height="7" viewBox="0 0 6 7"><path d="M1 1l3 2.5-3 2.5" fill="none" stroke="#fff" stroke-width="1.5"/></svg></span></div>

  <div class="rule" style="left:29px;top:684px;width:687px"></div>

  <h2 class="abs display why-title" style="font-weight:400">Why us?</h2>
  <p class="abs why-lead">We are devoted to your satisfaction and take a great deal of pride in our work.<br>Every specialist in our team is thoroughly trained and ready to help.</p>
  <div class="abs faq">?</div>
  <p class="abs why-copy" style="left:29px">Lorem ipsum dolor sit amet, con tuer adipiscing elitaesent ves tibulumle lacus. Aenean my hendrerit is. Phasellus porta. Fusce suscipit varius mi. Cum sociis natoque penati-bus et magnis dis parturient montes, nascetur ridiculus mus. Nulla dui. Fusce feugiat malesuada odio. Morbi nunc odio gravida at cursus nec</p>
  <p class="abs why-copy" style="left:320px">Tibulumle lacus. Aenean my hendrerit is. Phasellus porta. Fusce suscipit varius mi. Cum sociis natoque penatibus et magnis dis parturient montes, nascetur ridiculus mus. Nulla dui. Fusce feugiat malesuada odio. Morbi nunc odio gravida at, cursus nec, luctus a, lorem. Maecenas tristique orci ac sem.</p>

  <div class="rule" style="left:29px;top:895px;width:687px"></div>

  <div class="abs band"></div>
  <div class="divider" style="left:193px"></div>
  <div class="divider" style="left:369px"></div>
  <div class="divider" style="left:546px"></div>

  <section class="info" style="left:29px">
    <h3>About us</h3>
    <p>Lorem ipsum dolor sit amet, con tuer adipiscing elit.</p>
    <p>Lorem ipsum dolor sit amet, con tuer adipiscing elitaesent vestibu-lumle lacus. Aenean my hendrerit is. Phasellus porta. Fusce suscipit varius mi. Cum</p>
  </section>
  <section class="info" style="left:204px">
    <h3>Research</h3>
    <ul class="list" style="margin-top:0">
      <li><svg class="chev" viewBox="0 0 6 8"><path d="M1 1l3 3-3 3" fill="none" stroke="#1c1c1c" stroke-width="1.8"/></svg>Lorem ipsum dolor sit</li>
      <li><svg class="chev" viewBox="0 0 6 8"><path d="M1 1l3 3-3 3" fill="none" stroke="#1c1c1c" stroke-width="1.8"/></svg>Amet. Con tuer adipiscing</li>
      <li><svg class="chev" viewBox="0 0 6 8"><path d="M1 1l3 3-3 3" fill="none" stroke="#1c1c1c" stroke-width="1.8"/></svg>Elit. Praesent vestibulumle</li>
      <li><svg class="chev" viewBox="0 0 6 8"><path d="M1 1l3 3-3 3" fill="none" stroke="#1c1c1c" stroke-width="1.8"/></svg>Lacus. Aenean nonummy</li>
      <li><svg class="chev" viewBox="0 0 6 8"><path d="M1 1l3 3-3 3" fill="none" stroke="#1c1c1c" stroke-width="1.8"/></svg>Hendrerit is. Phasellus</li>
      <li><svg class="chev" viewBox="0 0 6 8"><path d="M1 1l3 3-3 3" fill="none" stroke="#1c1c1c" stroke-width="1.8"/></svg>Porta. Fusce suscip. Cum</li>
    </ul>
  </section>
  <section class="info" style="left:380px;top:930px">
    <h3>Testimonials</h3>
    <div class="bubble">Lorem ipsum dolor sit amet, con tuer adipiscing elit.</div>
    <div class="author">Jordan Reyes, Manager</div>
  </section>
  <section class="info" style="left:556px">
    <h3>Management</h3>
    <ul class="ticks">
      <li><span class="dot"><svg width="5" height="6" viewBox="0 0 5 6"><path d="M1 1l2 2-2 2" fill="none" stroke="#fff" stroke-width="1.3"/></svg></span>Lorem ipsum dolor sit amet, contuer adipiscing</li>
      <li><span class="dot"><svg width="5" height="6" viewBox="0 0 5 6"><path d="M1 1l2 2-2 2" fill="none" stroke="#fff" stroke-width="1.3"/></svg></span>Tuer adipiscing elitaesent mie lacus nonummy Praesent vestibulumle</li>
    </ul>
  </section>

  <div class="more" style="left:28px;top:1096px">More info <span class="go"><svg width="6" height="7" viewBox="0 0 6 7"><path d="M1 1l3 2.5-3 2.5" fill="none" stroke="#fff" stroke-width="1.5"/></svg></span></div>
  <div class="more" style="left:204px;top:1066px">More info <span class="go"><svg width="6" height="7" viewBox="0 0 6 7"><path d="M1 1l3 2.5-3 2.5" fill="none" stroke="#fff" stroke-width="1.5"/></svg></span></div>
  <div class="more" style="left:380px;top:1081px">More info <span class="go"><svg width="6" height="7" viewBox="0 0 6 7"><path d="M1 1l3 2.5-3 2.5" fill="none" stroke="#fff" stroke-width="1.5"/></svg></span></div>
  <div class="more" style="left:556px;top:1066px">More info <span class="go"><svg width="6" height="7" viewBox="0 0 6 7"><path d="M1 1l3 2.5-3 2.5" fill="none" stroke="#fff" stroke-width="1.5"/></svg></span></div>
</main>

<footer>
  <div class="abs brand foot-brand">
    <span class="brand-mark"></span>
    <div class="brand-name">SWIFTLINE<br>MOVERS</div>
  </div>
  <div class="abs copy">© 2011 Privacy Policy</div>
  <div class="abs foot-nav" style="left:302px">Home</div>
  <div class="abs foot-nav" style="left:356px">About us</div>
  <div class="abs foot-nav" style="left:424px">Services</div>
  <div class="abs foot-nav" style="left:488px">Products</div>
  <div class="abs foot-nav" style="left:556px">Partners</div>
  <div class="abs foot-nav" style="left:620px">News</div>
  <div class="abs foot-nav" style="left:670px">Contacts</div>
</footer>

</body>
</html>
```